Web Design Project

hi

i need an electronic store website designed. It should have light and warm colors like blue, green.

You will have to design the main page, product page, a normal page and also buttons and icons, boxes, etc. I will need the source files PSD/AI.

thanks

Industry/Entity Type

Electronic

```html
<!DOCTYPE html>
<html lang="en">
<head>
<meta charset="utf-8">
<title>Volt Home – Product</title>
<link href="https://fonts.googleapis.com/css2?family=PT+Sans:wght@400;700&family=Tinos:wght@700&display=swap" rel="stylesheet">
<style>
:root{
  --sky-top:#19def2;
  --sky-mid:#1aa3d9;
  --sky-deep:#0c6dab;
  --panel-a:#2f9bd8;
  --panel-b:#45c5f5;
  --tab:#1f9ad8;
  --accent:#1a8bd0;
  --orange:#f7941d;
  --ink:#333;
  --muted:#666;
  --rule:#dedede;
  --soft:#f7f7f7;
  --foot-dark:#0a4d7c;
  --foot-a:#0a5d93;
  --foot-b:#0b7dbd;
  --foot-head:#35c3ff;
}
*{box-sizing:border-box;margin:0;padding:0}
html,body{width:960px;height:1200px;overflow:hidden}
body{position:relative;background:#fff;font-family:"PT Sans",Tahoma,sans-serif;color:var(--ink)}
.abs{position:absolute}
.header-band{left:0;top:0;width:960px;height:280px;background:linear-gradient(180deg,var(--sky-top) 0%,var(--sky-mid) 35%,var(--sky-deep) 100%)}
.page-fade{left:0;top:280px;width:960px;height:40px;background:linear-gradient(180deg,#e9e9e9,#fff)}
.cart-info{left:684px;top:8px;font-size:12px;color:#fff}
.brand{left:54px;top:46px;font-size:27px;font-weight:700;color:#fff;letter-spacing:.2px}
.tagline{left:56px;top:73px;font-size:13px;color:#5ff0ff}
.nav{left:423px;top:61px;height:43px;display:flex}
.nav a{display:flex;align-items:center;justify-content:center;height:43px;color:#fff;font-size:12px;text-decoration:none;border-right:1px solid rgba(255,255,255,.25)}
.nav a:last-child{border-right:0}
.nav a.active{background:linear-gradient(180deg,#1690cf,#0b6aa8);border-top:3px solid #35b8ee}
.frame{left:7px;top:115px;width:936px;height:260px;background:#fff;border-radius:12px 12px 0 0}
.showcase{left:31px;top:124px;width:896px;height:243px;background:linear-gradient(180deg,var(--panel-a),var(--panel-b) 45%)}
.showcase-title{left:97px;top:138px;font-size:23px;color:#fff}
.showcase-rule{left:80px;top:165px;width:554px;height:1px;background:rgba(255,255,255,.45)}
.photo{background:linear-gradient(180deg,#3c4a55,#6e8ea6 50%,#2a2a2a)}
.tv{left:59px;top:190px;width:220px;height:155px;border-radius:4px}
.laptop{left:375px;top:188px;width:208px;height:160px;background:linear-gradient(180deg,#cfd3d6,#7fa5bf 40%,#c9cdd0);border-radius:4px}
.remote{left:725px;top:188px;width:66px;height:160px;background:linear-gradient(90deg,#e6e6e6,#fff 50%,#dcdcdc);border-radius:6px}
.tabs{left:0;top:360px}
.tab-label{font-size:16px;font-weight:700;color:#fff;letter-spacing:.5px}
.showcase-shadow{left:20px;top:392px;width:920px;height:14px;background:radial-gradient(ellipse at center,rgba(0,0,0,.12),transparent 70%)}
.side-head{left:52px;font-size:19px;color:var(--accent)}
.side-rule{left:40px;width:235px;height:1px;background:linear-gradient(90deg,var(--rule),#fff)}
.cat-list{left:54px;top:473px;width:210px;list-style:none}
.cat-list li{height:28.9px;border-bottom:1px solid var(--rule);font-size:11px;display:flex;align-items:center;padding-left:3px}
.cat-list li::before{content:"";width:0;height:0;border-left:3px solid #555;border-top:3px solid transparent;border-bottom:3px solid transparent;margin-right:6px}
.search-box{left:50px;top:760px;width:180px;height:27px;border:1px solid #d6d6d6;background:#fff}
.advanced{left:49px;top:798px;font-size:11px;font-weight:700;color:var(--muted);text-decoration:underline}
.btn{display:flex;align-items:center;justify-content:center;height:20px;border-radius:3px;background:linear-gradient(180deg,#5cc4f2,#1a86c6);color:#fff;font-size:11px;font-weight:700;box-shadow:0 1px 2px rgba(0,0,0,.25)}
.info-list{left:58px;top:882px;list-style:none;font-size:11px}
.info-list li{height:29px}
.content{left:303px;top:416px;width:617px;height:592px;background:var(--soft)}
.product-title{left:318px;top:427px;font-size:16px;color:var(--accent)}
.price{left:803px;top:424px;width:100px;text-align:right;font-family:"Tinos",Georgia,serif;font-weight:700;font-size:17px;color:#444}
.desc{left:318px;top:458px;width:450px;font-size:12px;line-height:18.3px;color:#444;font-family:Tahoma,"PT Sans",sans-serif}
.thumb{left:785px;top:456px;width:115px;height:115px;background:#fff;border:2px solid #e2e2e2;padding:16px 6px}
.thumb div{width:100%;height:100%}
.foot-bar{left:0;top:1017px;width:960px;height:51px;background:var(--foot-dark);border-top:2px solid #1a78b4}
.foot-links{left:35px;top:1037px;font-size:11px;color:#fff;display:flex;gap:0}
.foot-links span.sep{margin:0 16px}
.foot-main{left:0;top:1068px;width:960px;height:132px;background:linear-gradient(180deg,var(--foot-a),var(--foot-b))}
.foot-col{top:1085px;font-size:11px;color:#fff;line-height:18.4px}
.foot-col h4{font-size:11px;color:var(--foot-head);font-weight:700;letter-spacing:.3px}
.pay{top:1089px;width:46px;height:25px;background:linear-gradient(180deg,#fff,#e4e4e4);border-radius:2px;box-shadow:0 1px 2px rgba(0,0,0,.3)}
.pay-shade{top:1116px;width:46px;height:14px;background:linear-gradient(180deg,rgba(255,255,255,.25),transparent)}
</style>
</head>
<body>
<div class="abs header-band"></div>
<div class="abs page-fade"></div>

<header>
  <div class="abs cart-info">Shopping Cart items: 0 amount - $0.00</div>
  <div class="abs brand">Volt Home</div>
  <div class="abs tagline">shop with confidence</div>
  <nav class="abs nav">
    <a class="active" style="width:75px">Home</a>
    <a style="width:89px">My Account</a>
    <a style="width:80px">Checkout</a>
    <a style="width:92px">Shopping Cart</a>
    <a style="width:91px">About Us</a>
    <a style="width:110px">Contact Us</a>
  </nav>
</header>

<section class="showcase-wrap">
  <div class="abs frame"></div>
  <div class="abs showcase"></div>
  <div class="abs showcase-title">Browse over 100 products from our store</div>
  <div class="abs showcase-rule"></div>
  <div class="abs photo tv" role="img" aria-label="LCD monitor showing a lake and mountain landscape"></div>
  <div class="abs laptop" role="img" aria-label="Silver laptop showing a lake and mountain landscape"></div>
  <div class="abs remote" role="img" aria-label="White media remote control"></div>
  <svg class="abs tabs" width="960" height="34" viewBox="0 0 960 34">
    <g fill="#21a0dc">
      <polygon points="50,6 290,6 266,30 74,30"/>
      <polygon points="374,6 612,6 588,32 398,32"/>
      <polygon points="664,6 906,6 882,32 688,32"/>
    </g>
    <g fill="var(--orange)">
      <rect x="77" y="17" width="21" height="21" rx="3" transform="translate(0,-12)"/>
      <rect x="396" y="19" width="21" height="21" rx="3" transform="translate(0,-12)"/>
      <rect x="682" y="19" width="21" height="21" rx="3" transform="translate(0,-12)"/>
    </g>
    <g fill="none" stroke="#fff" stroke-width="2.4" stroke-linecap="round" stroke-linejoin="round">
      <path d="M82 15h11M89 11l4 4-4 4"/>
      <path d="M401 17h11M408 13l4 4-4 4"/>
      <path d="M687 17h11M694 13l4 4-4 4"/>
    </g>
    <text x="111" y="20" class="tab-label" font-family="PT Sans, sans-serif">LCD MONITORS</text>
    <text x="435" y="22" class="tab-label" font-family="PT Sans, sans-serif">LAPTOPS</text>
    <text x="720" y="22" class="tab-label" font-family="PT Sans, sans-serif">ACCESSORIES</text>
  </svg>
  <div class="abs showcase-shadow"></div>
</section>

<aside>
  <h2 class="abs side-head" style="top:423px;font-weight:400">CATEGORIES</h2>
  <div class="abs side-rule" style="top:450px"></div>
  <svg class="abs" style="left:96px;top:450px" width="22" height="12"><polygon points="0,0 22,0 11,11" fill="#e6e6e6"/></svg>
  <ul class="abs cat-list">
    <li>Audio Systems</li><li>Cameras (1)</li><li>Computers (1)</li><li>Home Security (1)</li>
    <li>Home Theater (1)</li><li>Kitchen (1)</li><li>Mobile Phones</li><li>TV (2)</li>
  </ul>

  <h2 class="abs side-head" style="top:713px;font-weight:400">SEARCH</h2>
  <div class="abs side-rule" style="top:740px"></div>
  <svg class="abs" style="left:96px;top:740px" width="22" height="12"><polygon points="0,0 22,0 11,11" fill="#e6e6e6"/></svg>
  <div class="abs search-box"></div>
  <div class="abs advanced">advanced</div>
  <div class="abs btn" style="left:177px;top:798px;width:63px">SEARCH</div>

  <h2 class="abs side-head" style="top:833px;font-weight:400">INFORMATION</h2>
  <div class="abs side-rule" style="top:860px"></div>
  <svg class="abs" style="left:96px;top:860px" width="22" height="12"><polygon points="0,0 22,0 11,11" fill="#e6e6e6"/></svg>
  <ul class="abs info-list"><li>Shipping</li><li>Privacy</li><li>About Us</li></ul>
</aside>

<main>
  <div class="abs content"></div>
  <h1 class="abs product-title" style="font-weight:400">product1</h1>
  <div class="abs price">$33.00</div>
  <p class="abs desc">Vivamus felis. Negestas ipsum. Fusce in Vivamus felis. Negestas ipsum. Fusce in Vivamus felis. Negestas ipsum. Fusce in Vivamus felis. Negestas ipsum. Fusce in Vivamus felis. Negestas ipsum. Fusce in Vivamus felis. Negestas ipsum. Fusce in Vivamus felis. Negestas ipsum. Fusce in Vivamus felis. Negestas ipsum. Fusce in Vivamus felis. Negestas ipsum. Fusce in Vivamus felis. Negestas ipsum. Fusce in Vivamus felis. Negestas ipsum. Fusce in Vivamus felis. Negestas ipsum. Fusce in Vivamus felis. Negestas ipsum. Fusce in Vivamus felis. Negestas ipsum. Fusce in Vivamus felis. Negestas ipsum. Fusce in Vivamus felis. Negestas ipsum. Fusce in Vivamus felis. Negestas ipsum. Fusce in Vivamus felis. Negestas ipsum. Fusce in Vivamus felis. Negestas ipsum. Fusce in Vivamus felis. Negestas ipsum. Fusce in Vivamus felis. Negestas ipsum. Fusce in Vivamus felis. Negestas ipsum. Fusce in</p>
  <div class="abs thumb"><div class="photo" role="img" aria-label="Product photo of an LCD television showing a landscape"></div></div>
  <div class="abs btn" style="left:327px;top:695px;width:85px">REVIEWS</div>
  <div class="abs btn" style="left:813px;top:697px;width:85px">ADD TO CART</div>
</main>

<footer>
  <div class="abs foot-bar"></div>
  <div class="abs foot-links">
    <span>Copyright © 2013. All Rights Reserved. Storefront Templates</span>
    <span style="margin-left:12px">Home</span><span class="sep">|</span>
    <span>Shipping</span><span class="sep">|</span>
    <span>Privacy</span><span class="sep">|</span>
    <span>About Us</span>
  </div>
  <div class="abs foot-main"></div>
  <div class="abs foot-col" style="left:37px">
    <h4>OFFICE INFORMATION:</h4>
    Volt Home<br>48 Harbor Lane<br>Westbrook<br>Maine,<br>04092, United States
  </div>
  <div class="abs foot-col" style="left:217px">
    <h4>CONTACT INFORMATION:</h4>
    Call us: (Int) 002 (41) 508 7713<br>Fax: (Int) 002 (41) 508 7713<br>Office hours: 8.00am - 4:00pm GMT+5
  </div>
  <div class="abs pay" style="left:644px"></div>
  <div class="abs pay" style="left:700px"></div>
  <div class="abs pay" style="left:756px"></div>
  <div class="abs pay" style="left:812px"></div>
  <div class="abs pay" style="left:868px"></div>
  <div class="abs pay-shade" style="left:644px"></div>
  <div class="abs pay-shade" style="left:700px"></div>
  <div class="abs pay-shade" style="left:756px"></div>
  <div class="abs pay-shade" style="left:812px"></div>
  <div class="abs pay-shade" style="left:868px"></div>
</footer>
</body>
</html>
```